Unique and original Business Card for Financial Services Business

I have moved premises and need to change the detail on my business card so thought now is a good time for a re-design. Looking for something professional and modern with colours to fit in with out logo. Like the idea of foil or embossing if that works but not a must have but I do want something that stands out and that I could not design myself.

Once business card is designed I will also be looking to get letterhead and flyers done but want the business card concept in place first.

The majority of designs I am receiving are generic and template based. I am looking for something unique and original. We have some great design elements in our logo, think outside the box and show me something that stands out from the crowd.

Target Market(s)

Business Professionals

Industry/Entity Type

Finance

Contact Information for Business Card

Name: Delia Norwood Phone 0473 958 162 Address PO Box 8617 Mossvale NSW 2389 Email info@steadyharbourfinancialservices.com.au website www.steadyharbourfinancialservices.com.au

Font styles to use
Other font styles liked:
• Ralway

Requirements
Should not have
• No black backgrounds please

```html
<!DOCTYPE html>
<html lang="en">
<head>
<meta charset="utf-8">
<title>Steady Harbour Financial Services – Business Card</title>
<link rel="stylesheet" href="https://fonts.googleapis.com/css2?family=Raleway:wght@300;400&family=Open+Sans:wght@400;700&display=swap">
<style>
  :root {
    --backdrop: #d9d2c6;
    --card: #ffffff;
    --teal: #0e9a98;
    --teal-deep: #05606b;
    --teal-bright: #12aaa3;
    --silver: #b9bcbf;
    --silver-dark: #8d9196;
    --ink-grey: #555a5e;
    --on-teal: #ffffff;
  }
  * { margin: 0; padding: 0; box-sizing: border-box; }
  html, body { width: 1200px; height: 985px; overflow: hidden; }
  body { background: var(--backdrop); position: relative; }

  .card {
    position: absolute;
    width: 640px;
    height: 366px;
    background: var(--card);
    border-radius: 30px;
    overflow: hidden;
    box-shadow: 0 14px 30px rgba(70, 55, 35, 0.22);
  }
  .card--front { left: 60px; top: 70px; }
  .card--back { left: 500px; top: 545px; }

  .brand {
    position: absolute;
    display: flex;
    align-items: center;
    gap: 18px;
  }
  .brand__dot {
    flex: none;
    border-radius: 50%;
    background: var(--teal);
  }
  .brand__name {
    font-family: "Raleway", sans-serif;
    font-weight: 300;
    color: var(--teal);
    text-transform: uppercase;
    line-height: 1.15;
    white-space: nowrap;
  }
  .card--front .brand { left: 80px; top: 118px; }
  .card--front .brand__dot { width: 96px; height: 96px; }
  .card--front .brand__name { font-size: 40px; letter-spacing: 1px; }

  .card--back .brand { left: 40px; top: 40px; gap: 12px; }
  .card--back .brand__dot { width: 58px; height: 58px; }
  .card--back .brand__name { font-size: 17px; letter-spacing: 0.4px; }

  .wave { position: absolute; inset: 0; width: 640px; height: 366px; }

  .holder {
    position: absolute;
    right: 48px;
    top: 30px;
    text-align: right;
    font-family: "Open Sans", sans-serif;
  }
  .holder__name {
    color: var(--teal);
    font-weight: 700;
    font-size: 26px;
    line-height: 1.3;
    letter-spacing: 0.5px;
    text-transform: uppercase;
  }
  .holder__title {
    color: var(--ink-grey);
    font-size: 14px;
    line-height: 1.3;
  }

  .contact {
    position: absolute;
    right: 30px;
    top: 150px;
    list-style: none;
    font-family: "Open Sans", sans-serif;
    font-size: 13px;
    color: var(--on-teal);
    text-align: right;
    line-height: 1.45;
  }
  .contact__item {
    display: flex;
    justify-content: flex-end;
    align-items: flex-start;
    gap: 10px;
    margin-bottom: 3px;
    white-space: nowrap;
  }
  .contact__icon { flex: none; width: 12px; height: 12px; margin-top: 3px; fill: var(--on-teal); }
</style>
</head>
<body>

<section class="card card--front" aria-label="Business card front">
  <div class="brand">
    <span class="brand__dot"></span>
    <p class="brand__name">Steady Harbour<br>Financial Services</p>
  </div>
</section>

<section class="card card--back" aria-label="Business card back">
  <svg class="wave" viewBox="0 0 640 366" aria-hidden="true">
    <defs>
      <linearGradient id="teal-band" x1="0" y1="1" x2="1" y2="0">
        <stop offset="0" stop-color="var(--teal-deep)"/>
        <stop offset="0.5" stop-color="var(--teal-bright)"/>
        <stop offset="1" stop-color="var(--teal-deep)"/>
      </linearGradient>
      <linearGradient id="silver-band" x1="0" y1="0" x2="1" y2="0">
        <stop offset="0" stop-color="var(--silver)"/>
        <stop offset="1" stop-color="var(--silver-dark)"/>
      </linearGradient>
    </defs>
    <path d="M0,288 C160,288 222,240 262,160 C302,88 418,106 640,102 L640,366 L0,366 Z" fill="url(#silver-band)"/>
    <path d="M0,298 C163,298 230,250 270,170 C310,98 422,116 640,112 L640,366 L0,366 Z" fill="#ffffff"/>
    <path d="M0,304 C165,304 236,256 276,176 C316,104 424,124 640,118 L640,366 L0,366 Z" fill="url(#teal-band)"/>
  </svg>

  <div class="brand">
    <span class="brand__dot"></span>
    <p class="brand__name">Steady Harbour<br>Financial Services</p>
  </div>

  <header class="holder">
    <h1 class="holder__name">Delia Norwood</h1>
    <p class="holder__title">Founder &amp; CEO</p>
  </header>

  <ul class="contact">
    <li class="contact__item">
      <span>PO Box 8617<br>Mossvale, NSW 2389</span>
      <svg class="contact__icon" viewBox="0 0 12 12" aria-hidden="true"><path d="M6 0a4 4 0 0 0-4 4c0 3 4 8 4 8s4-5 4-8a4 4 0 0 0-4-4zm0 5.6A1.6 1.6 0 1 1 6 2.4a1.6 1.6 0 0 1 0 3.2z"/></svg>
    </li>
    <li class="contact__item">
      <span>0473 958 162</span>
      <svg class="contact__icon" viewBox="0 0 12 12" aria-hidden="true"><path d="M2.4 0.6l1.8 0 0.8 2.6-1.2 1a7 7 0 0 0 3 3l1-1.2 2.6 0.8 0 1.8c0 0.8-0.7 1.4-1.5 1.3C4.3 9.4 2.6 7.7 1.1 2.1 1 1.3 1.6 0.6 2.4 0.6z"/></svg>
    </li>
    <li class="contact__item">
      <span>info@steadyharbourfinancialservices.com.au</span>
      <svg class="contact__icon" viewBox="0 0 12 12" aria-hidden="true"><path d="M0 2h12v8H0z M0.8 2.6 6 6.6 11.2 2.6" fill="none" stroke="#fff" stroke-width="1.2"/></svg>
    </li>
    <li class="contact__item">
      <span>www.steadyharbourfinancialservices.com.au</span>
      <svg class="contact__icon" viewBox="0 0 12 12" aria-hidden="true"><circle cx="6" cy="6" r="5.3" fill="none" stroke="#fff" stroke-width="1.2"/><path d="M0.7 6h10.6M6 0.7c-3 3-3 7.6 0 10.6M6 0.7c3 3 3 7.6 0 10.6" fill="none" stroke="#fff" stroke-width="1"/></svg>
    </li>
  </ul>
</section>

</body>
</html>
```